User Frontend Design for Support Logging System

I have a PHP web application to manage IT support calls and require a front-end design and user logon screen.

I have attached the current design which needs improving.

I have 2 current designs. The 2nd design is one I have been working on but requires a "professional touch". I also require the tables designed with dummy data from the 1st design.

I have attached my company logo in AI format which I would like incorporated into the design. There should also be a placeholder to supply the users company name upon login.

The screenshots I have attached should explain what I am looking for.

The Home Page should include charts which show statistical information such as:
Number of support tickets logged per month. Bar Chart etc.
Number of currently open support tickets.
Number of Quote Requests awaiting a response.
Number of Files and file repository.
Number of Reports.
Number of Customers.

For the Jobs and Customers pages the table fields should be designed as per the attached screenshots but a better looking tables. The table options such as uploading a file and adding a customer - these options can be changed and displayed differently.

Quotes page should display quotes returned and a "request a quote form".

Files page should have a good structure for browsing through an archive of files.

Profile page should have the option to include a profile picture.

An additional side page should be created for a web based calendar (these calendar entries will be updated by code).

The navbar should also include an alerts section.
The current attached design I have is based on bootstraps navbar.

Inspiration: http://pelvoriad.com/freebie/free-admin-templates-for-backend-panels/

Hopefully this above link will show you some navigation style designs that I am looking for.

Please note, I will be doing the PHP coding myself and it is just the page designs I require in either HTML and or PHP format. I also require the CSS files for this project.
I need the code in a format where I can add and remove items in the menu from the code and not PSD/image based format.

If you think this project requires a higher budget let me know what you would expect and I will increase it!

Any questions, please let me know.
Dummy data can be shown for design purposes.

I have provided you a dummy login to our current system to show you the system:
https://ridge.brivelnetworks.co.uk/
username: dan.prewett@brivelnetworks.co.uk
password:P@55w0rd

```html
<!DOCTYPE html>
<html lang="en">
<head>
<meta charset="utf-8">
<title>Dashboard – Brivel Networks Support</title>
<link href="https://fonts.googleapis.com/css2?family=Open+Sans:wght@300;400;600;700&family=Roboto+Condensed:wght@700&display=swap" rel="stylesheet">
<style>
:root{
  --brand-blue:#2356a8;
  --title-blue:#2b62b3;
  --sidebar:#6b6b6b;
  --sidebar-dark:#2d2d2d;
  --footer:#2b2b2b;
  --strip:#e9e9e9;
  --red:#e84130;
  --orange:#f0ad4e;
  --grey:#8a8a8a;
  --light-tile:#e6e6e6;
  --border:#d9d9d9;
  --text:#444;
  --muted:#999;
}
*{box-sizing:border-box;margin:0;padding:0}
html,body{width:1138px;height:1200px;overflow:hidden}
body{position:relative;font-family:"Open Sans",Arial,sans-serif;color:var(--text);background:#fff;font-size:12px}
.abs{position:absolute}
.topbar{left:0;top:0;width:1138px;height:110px;background:var(--brand-blue)}
.brand{left:28px;top:12px;width:200px;height:84px;display:flex;align-items:center;gap:10px;color:#fff}
.brand-ring{width:58px;height:58px;border:3px solid #fff;border-radius:50%;flex:none}
.brand-name{font-size:19px;font-weight:600;line-height:1.15}
.topnav{left:254px;top:6px;display:flex;gap:30px;color:#fff;font-size:10.5px}
.user{right:44px;top:6px;color:#fff;font-size:11.5px}
.title-bar{left:250px;top:27px;width:847px;height:83px;background:linear-gradient(#fff,#f4f4f4)}
.title-bar h1{position:absolute;left:14px;top:27px;font-weight:300;font-size:26px;color:var(--title-blue)}
.strip{left:1097px;top:110px;width:41px;height:1047px;background:var(--strip)}
.sidebar{left:0;top:110px;width:250px;height:1047px;background:var(--sidebar)}
.search-band{left:0;top:0;width:250px;height:54px;background:var(--sidebar-dark)}
.search{left:22px;top:14px;width:206px;height:26px;background:#222;border:1px solid #3a3a3a;color:#555;font-size:11px;padding:6px 12px}
.search svg{position:absolute;right:7px;top:6px}
.menu{left:22px;top:86px;width:228px;list-style:none}
.menu li{height:38.5px;display:flex;align-items:center;gap:8px;padding-left:12px;color:#fff;font-size:11px;border-bottom:1px solid #5a5a5a;box-shadow:0 1px 0 #7a7a7a}
.menu li.active{background:#fff;color:var(--brand-blue);font-weight:600;font-size:12px;height:37px;margin-bottom:8px;border:none;box-shadow:none}
.content{left:250px;top:110px;width:847px;height:1047px;background:#fff}
.tile{height:86px;width:178px;top:135px;color:#fff;font-family:"Roboto Condensed",sans-serif;font-size:20px;overflow:hidden}
.tile span{position:absolute;left:15px;top:17px}
.tile .play{position:absolute;right:8px;top:8px}
.tile .deco{position:absolute;right:0;bottom:0}
.t-jobs{left:281px;background:var(--red)}
.t-cust{left:483px;background:var(--orange)}
.t-rep{left:685px;background:var(--grey)}
.t-quote{left:887px;background:var(--light-tile);color:#a5a5a5}
.panel{border:1px solid var(--border);background:#fff}
.panel-head{position:absolute;left:0;top:0;right:0;height:33px;background:linear-gradient(#f9f9f9,#ececec);border-bottom:1px solid var(--border);display:flex;align-items:center;gap:8px;padding-left:13px;font-size:13px;color:#444;z-index:2}
.panel svg.body{position:absolute;left:-1px;top:-1px}
.btns{position:absolute;top:52px;display:flex;z-index:2}
.btns div{border:1px solid #ccc;height:24px;padding:0 9px;display:flex;align-items:center;font-size:10px;color:#333;background:#fff}
.btns div+div{border-left:none}
.btns .on{background:#e6e6e6}
.rule{position:absolute;left:13px;right:13px;top:93px;border-top:1px solid #eee}
.to-top{left:1044px;top:756px;width:33px;height:36px;background:#333;display:flex;align-items:center;justify-content:center}
.footer{left:0;top:1157px;width:1138px;height:43px;background:var(--footer);color:#fff;font-size:10.5px;display:flex;align-items:center;justify-content:center}
svg text{font-family:"Open Sans",Arial,sans-serif}
</style>
</head>
<body>

<header class="abs topbar"></header>
<div class="abs brand"><div class="brand-ring"></div><div class="brand-name">Brivel<br>Networks Ltd.</div></div>
<nav class="abs topnav"><span>⌂ Home</span><span>Dropdown ▾</span></nav>
<div class="abs user">● Dan Prewett</div>
<div class="abs title-bar"><h1>Dashboard</h1></div>
<div class="abs strip"></div>

<aside class="abs sidebar">
  <div class="abs search-band"></div>
  <div class="abs search">Search
    <svg width="13" height="13" viewBox="0 0 13 13"><circle cx="5.5" cy="5.5" r="4" fill="none" stroke="#666" stroke-width="1.8"/><path d="M8.5 8.5L12 12" stroke="#666" stroke-width="2"/></svg>
  </div>
  <ul class="abs menu">
    <li class="active"><svg width="14" height="12" viewBox="0 0 14 12"><path d="M7 0L0 6h2v6h4V8h2v4h4V6h2z" fill="#2356a8"/></svg>Home</li>
    <li><svg width="10" height="11"><rect x="1" y="0" width="8" height="11" fill="#ddd"/></svg>Jobs</li>
    <li><svg width="14" height="11"><rect width="14" height="11" fill="#ddd"/><path d="M0 4h14M0 7h14" stroke="#6b6b6b"/></svg>Customers</li>
    <li><svg width="14" height="11"><rect x="0.5" y="0.5" width="13" height="8" fill="none" stroke="#ddd"/><rect x="4" y="9" width="6" height="2" fill="#ddd"/></svg>Chart</li>
    <li><svg width="14" height="11"><rect x="0.5" y="0.5" width="13" height="10" fill="none" stroke="#ddd"/><path d="M0 4h14M0 7h14M5 0v11" stroke="#ddd"/></svg>Quote</li>
    <li><svg width="14" height="11"><rect width="14" height="11" fill="#ddd"/><path d="M0 4h14M0 7h14" stroke="#6b6b6b"/></svg>Files</li>
    <li><svg width="14" height="11"><rect x="0.5" y="0.5" width="13" height="10" fill="none" stroke="#ddd"/><path d="M3 9V6M6 9V3M9 9V5M12 9V2" stroke="#ddd" stroke-width="1.5"/></svg>Reports</li>
    <li><svg width="10" height="11"><rect x="0.5" y="0.5" width="9" height="10" fill="none" stroke="#ddd"/></svg>Lorem</li>
  </ul>
</aside>

<main class="abs content"></main>

<!-- Summary tiles -->
<div class="abs tile t-jobs"><span>JOBS</span>
  <svg class="play" width="11" height="11"><circle cx="5.5" cy="5.5" r="5.5" fill="rgba(0,0,0,.25)"/><path d="M4 3l4 2.5L4 8z" fill="var(--red)"/></svg>
  <svg class="deco" width="70" height="60" viewBox="0 0 70 60"><path d="M35 0l9 20 21 3-15 14 4 21-19-10-19 10 4-21L5 23l21-3z" fill="rgba(200,20,10,.45)"/></svg>
</div>
<div class="abs tile t-cust"><span>CUSTOMERS</span>
  <svg class="play" width="11" height="11"><circle cx="5.5" cy="5.5" r="5.5" fill="rgba(0,0,0,.2)"/><path d="M4 3l4 2.5L4 8z" fill="var(--orange)"/></svg>
  <svg class="deco" width="75" height="60" viewBox="0 0 75 60"><path d="M5 20l50-18 10 28-45 16z" fill="rgba(220,130,20,.45)"/><circle cx="30" cy="54" r="5" fill="rgba(220,130,20,.45)"/><circle cx="58" cy="46" r="5" fill="rgba(220,130,20,.45)"/></svg>
</div>
<div class="abs tile t-rep"><span>REPORTS</span>
  <svg class="play" width="11" height="11"><circle cx="5.5" cy="5.5" r="5.5" fill="rgba(0,0,0,.25)"/><path d="M4 3l4 2.5L4 8z" fill="var(--grey)"/></svg>
  <svg class="deco" width="55" height="60" viewBox="0 0 55 60"><circle cx="38" cy="38" r="28" fill="none" stroke="rgba(60,60,60,.35)" stroke-width="7"/><path d="M38 22v17l-10 8" stroke="rgba(60,60,60,.35)" stroke-width="6" fill="none"/></svg>
</div>
<div class="abs tile t-quote"><span>QUOTE</span>
  <svg class="play" width="11" height="11"><circle cx="5.5" cy="5.5" r="5.5" fill="#bbb"/><path d="M4 3l4 2.5L4 8z" fill="var(--light-tile)"/></svg>
  <svg class="deco" width="75" height="60" viewBox="0 0 75 60"><g transform="rotate(-25 40 35)"><rect x="8" y="18" width="66" height="36" fill="none" stroke="#d2d2d2" stroke-width="5"/><circle cx="41" cy="36" r="10" fill="#d2d2d2"/></g></svg>
</div>

<!-- Area chart -->
<section class="abs panel" style="left:281px;top:243px;width:581px;height:326px">
  <div class="panel-head"><svg width="13" height="11"><rect x="0.5" y="0.5" width="12" height="10" fill="none" stroke="#888"/><path d="M3 9V6M6 9V3M9 9V5" stroke="#888" stroke-width="1.5"/></svg>Area Chart</div>
  <div class="btns" style="left:13px"><div>Day</div><div>Week</div><div class="on">Month</div></div>
  <div class="btns" style="left:144px"><div>Custom Date ▾</div></div>
  <div class="btns" style="left:531px"><div>⚙ ▾</div></div>
  <div class="rule"></div>
  <svg class="body" width="581" height="326" viewBox="346 299 714 400">
    <g stroke="#e3e3e3"><path d="M428 459H1020M428 504H1020M428 550H1020M428 595H1020M428 641H1020"/></g>
    <g font-size="12" fill="#666" text-anchor="end"><text x="416" y="463">26,215</text><text x="416" y="508">19,661</text><text x="416" y="554">13,108</text><text x="416" y="599">6,554</text><text x="416" y="645">0</text></g>
    <g font-size="12" fill="#666" text-anchor="middle"><text x="648" y="661">2011</text><text x="911" y="661">2012</text></g>
    <path d="M428 604L494 589 560 576 626 550 691 564 757 558 823 570 889 459 954 522 1020 530V641H428Z" fill="#a3a3a3"/>
    <path d="M428 622L494 606 560 593 626 590 691 581 757 572 823 580 889 495 954 536 1020 542V641H428Z" fill="#ebcba0"/>
    <path d="M428 622L494 622 560 606 626 614 691 594 757 601 823 607 889 536 954 567 1020 582V641H428Z" fill="#de8077"/>
    <polyline points="428,604 494,589 560,576 626,550 691,564 757,558 823,570 889,459 954,522 1020,530" fill="none" stroke="#7a7a7a" stroke-width="3" stroke-linejoin="round"/>
    <polyline points="428,622 494,606 560,593 626,590 691,581 757,572 823,580 889,495 954,536 1020,542" fill="none" stroke="#f0a030" stroke-width="2" stroke-linejoin="round"/>
    <polyline points="428,622 494,622 560,606 626,614 691,594 757,601 823,607 889,536 954,567 1020,582" fill="none" stroke="#e03a2a" stroke-width="2" stroke-linejoin="round"/>
    <g fill="#fff" stroke-width="1.2">
      <g stroke="#7a7a7a"><circle cx="494" cy="589" r="2.8"/><circle cx="560" cy="576" r="2.8"/><circle cx="626" cy="550" r="2.8"/><circle cx="691" cy="564" r="2.8"/><circle cx="757" cy="558" r="2.8"/><circle cx="823" cy="570" r="2.8"/><circle cx="889" cy="459" r="2.8"/><circle cx="954" cy="522" r="2.8"/><circle cx="1020" cy="530" r="2.8"/></g>
      <g stroke="#f0a030"><circle cx="494" cy="606" r="2.8"/><circle cx="560" cy="593" r="2.8"/><circle cx="626" cy="590" r="2.8"/><circle cx="691" cy="581" r="2.8"/><circle cx="757" cy="572" r="2.8"/><circle cx="823" cy="580" r="2.8"/><circle cx="889" cy="495" r="2.8"/><circle cx="954" cy="536" r="2.8"/><circle cx="1020" cy="542" r="2.8"/></g>
      <g stroke="#e03a2a"><circle cx="428" cy="622" r="2.8"/><circle cx="494" cy="622" r="2.8"/><circle cx="560" cy="606" r="2.8"/><circle cx="626" cy="614" r="2.8"/><circle cx="691" cy="594" r="2.8"/><circle cx="757" cy="601" r="2.8"/><circle cx="823" cy="607" r="2.8"/><circle cx="889" cy="536" r="2.8"/><circle cx="954" cy="567" r="2.8"/><circle cx="1020" cy="582" r="2.8"/></g>
    </g>
  </svg>
</section>

<!-- Donut chart -->
<section class="abs panel" style="left:887px;top:243px;width:177px;height:268px">
  <div class="panel-head"><svg width="13" height="11"><rect x="0.5" y="0.5" width="12" height="10" fill="none" stroke="#888"/><path d="M3 9V6M6 9V3M9 9V5" stroke="#888" stroke-width="1.5"/></svg>Donut Chart</div>
  <svg class="body" width="177" height="268" viewBox="1091 299 218 330">
    <g fill="none" transform="rotate(0 1199 485)">
      <circle cx="1199" cy="485" r="72" stroke="var(--red)" stroke-width="11" stroke-dasharray="122 330" transform="rotate(2 1199 485)"/>
      <circle cx="1199" cy="485" r="72" stroke="#8a8a8a" stroke-width="11" stroke-dasharray="60 392" transform="rotate(103 1199 485)"/>
      <circle cx="1199" cy="485" r="72" stroke="#444" stroke-width="11" stroke-dasharray="100 352" transform="rotate(152 1199 485)"/>
      <circle cx="1199" cy="485" r="74" stroke="var(--orange)" stroke-width="16" stroke-dasharray="157 300" transform="rotate(233 1199 485)"/>
    </g>
    <text x="1199" y="481" text-anchor="middle" font-size="21" font-weight="700" fill="#111">Referrals</text>
    <text x="1199" y="505" text-anchor="middle" font-size="15" fill="#111">40%</text>
  </svg>
</section>

<!-- Logged per month -->
<section class="abs panel" style="left:887px;top:532px;width:177px;height:255px">
  <div class="panel-head"><svg width="11" height="11"><circle cx="5.5" cy="5.5" r="4.5" fill="none" stroke="#666" stroke-width="1.4"/><path d="M5.5 3v3l2 1" stroke="#666" fill="none"/></svg>Logged per month</div>
  <svg class="body" width="177" height="255" viewBox="1091 655 218 314">
    <defs><pattern id="stripes" width="14" height="14" patternUnits="userSpaceOnUse" patternTransform="rotate(45)"><rect width="7" height="14" fill="rgba(255,255,255,.18)"/></pattern></defs>
    <g font-size="13" fill="#777"><text x="1107" y="736">% Support tickets</text><text x="1107" y="816">% Reports</text><text x="1105" y="890">% Customers</text></g>
    <g font-size="15" fill="#555" text-anchor="end"><text x="1293" y="737">77.7%</text><text x="1293" y="816">33.2%</text><text x="1291" y="888">42.7%</text></g>
    <rect x="1107" y="750" width="186" height="19" fill="#f2f2f2"/><rect x="1107" y="750" width="143" height="19" fill="var(--red)"/><rect x="1107" y="750" width="143" height="19" fill="url(#stripes)"/>
    <rect x="1107" y="827" width="186" height="19" fill="#f2f2f2"/><rect x="1107" y="827" width="62" height="19" fill="#8a8a8a"/><rect x="1107" y="827" width="62" height="19" fill="url(#stripes)"/>
    <rect x="1106" y="901" width="185" height="19" fill="#f2f2f2"/><rect x="1106" y="901" width="78" height="19" fill="var(--orange)"/><rect x="1106" y="901" width="78" height="19" fill="url(#stripes)"/>
  </svg>
</section>
<div class="abs to-top"><svg width="14" height="9"><path d="M1 8l6-6 6 6" stroke="#fff" stroke-width="2.4" fill="none"/></svg></div>

<!-- Sales summary -->
<svg class="abs" style="left:885px;top:798px" width="180" height="168" viewBox="1088 982 221 207">
  <rect x="1088" y="982" width="221" height="207" fill="#fff" stroke="#ddd"/>
  <rect x="1088" y="982" width="221" height="118" fill="#38a6e0"/>
  <text x="1098" y="1004" font-size="11" font-weight="700" fill="#fff">SALE</text>
  <text x="1298" y="1004" font-size="11" font-weight="700" fill="#fff" text-anchor="end">$1,890,65</text>
  <text x="1098" y="1019" font-size="7.5" fill="#fff">Today 8:43 AM</text>
  <text x="1298" y="1019" font-size="7.5" fill="#fff" text-anchor="end">+$432,50 (15,78%)</text>
  <polyline points="1100,1062 1115,1052 1130,1060 1155,1044 1175,1052 1200,1050 1225,1046 1250,1044 1275,1046 1298,1049" fill="none" stroke="#fff" stroke-width="2"/>
  <g fill="rgba(255,255,255,.35)"><rect x="1100" y="1085" width="3" height="8"/><rect x="1113" y="1080" width="3" height="13"/><rect x="1126" y="1082" width="3" height="11"/><rect x="1139" y="1077" width="3" height="16"/><rect x="1152" y="1075" width="3" height="18"/><rect x="1165" y="1079" width="3" height="14"/><rect x="1178" y="1081" width="3" height="12"/><rect x="1191" y="1076" width="3" height="17"/><rect x="1204" y="1078" width="3" height="15"/><rect x="1217" y="1074" width="3" height="19"/><rect x="1230" y="1077" width="3" height="16"/><rect x="1243" y="1073" width="3" height="20"/><rect x="1256" y="1075" width="3" height="18"/><rect x="1269" y="1072" width="3" height="21"/><rect x="1282" y="1076" width="3" height="17"/><rect x="1295" y="1074" width="3" height="19"/></g>
  <text x="1099" y="1125" font-size="12" fill="#555">+$780,98</text>
  <text x="1099" y="1141" font-size="7.5" fill="#aaa">Weekly Change</text>
  <g fill="#e6e6e6"><rect x="1207" y="1110" width="9" height="20"/><rect x="1220" y="1110" width="9" height="20"/><rect x="1233" y="1110" width="9" height="20"/><rect x="1246" y="1110" width="9" height="20"/><rect x="1259" y="1110" width="9" height="20"/><rect x="1272" y="1110" width="9" height="20"/><rect x="1285" y="1110" width="9" height="20"/></g>
  <rect x="1207" y="1123" width="9" height="7" fill="#8ec9ea"/>
  <g font-size="6.5" fill="#aaa" text-anchor="middle"><text x="1211" y="1140">M</text><text x="1224" y="1140">T</text><text x="1237" y="1140">W</text><text x="1250" y="1140">T</text><text x="1263" y="1140">F</text><text x="1276" y="1140">S</text><text x="1289" y="1140">S</text></g>
  <path d="M1088 1149H1309M1198 1149V1189" stroke="#e3e3e3"/>
  <text x="1099" y="1165" font-size="12" fill="#555">9.127</text>
  <text x="1099" y="1180" font-size="7.5" fill="#aaa">Deals</text>
  <text x="1298" y="1165" font-size="12" fill="#555" text-anchor="end">$189.783,87</text>
  <text x="1298" y="1180" font-size="7.5" fill="#aaa" text-anchor="end">Total Income</text>
</svg>

<!-- Bar chart -->
<section class="abs panel" style="left:888px;top:983px;width:177px;height:128px">
  <div class="panel-head"><svg width="13" height="11"><rect x="0.5" y="0.5" width="12" height="10" fill="none" stroke="#888"/><path d="M3 9V6M6 9V3M9 9V5" stroke="#888" stroke-width="1.5"/></svg>Bar Chart</div>
  <svg class="body" width="177" height="128" viewBox="1092 1209 218 158">
    <g fill="var(--red)"><rect x="1122" y="1292" width="4" height="3"/><rect x="1129" y="1282" width="4" height="13"/><rect x="1136" y="1276" width="4" height="19"/><rect x="1143" y="1268" width="4" height="27"/><rect x="1150" y="1272" width="4" height="23"/><rect x="1157" y="1264" width="4" height="31"/><rect x="1164" y="1274" width="4" height="21"/><rect x="1171" y="1260" width="4" height="35"/></g>
    <g fill="#444"><rect x="1230" y="1290" width="4" height="5"/><rect x="1237" y="1280" width="4" height="15"/><rect x="1244" y="1272" width="4" height="23"/><rect x="1251" y="1264" width="4" height="31"/><rect x="1258" y="1268" width="4" height="27"/><rect x="1265" y="1272" width="4" height="23"/><rect x="1272" y="1266" width="4" height="29"/><rect x="1279" y="1260" width="4" height="35"/></g>
    <g text-anchor="middle" fill="#333"><text x="1148" y="1324" font-size="16">1,564</text><text x="1256" y="1324" font-size="16">872</text><text x="1148" y="1346" font-size="13">Total Visits</text><text x="1256" y="1346" font-size="13">New Visits</text></g>
  </svg>
</section>

<!-- Calendar -->
<section class="abs panel" style="left:284px;top:586px;width:580px;height:523px">
  <div class="panel-head"><svg width="12" height="12"><rect x="0.5" y="2" width="11" height="9.5" fill="none" stroke="#888"/><path d="M0 5h12M3 0v3M9 0v3" stroke="#888"/></svg>Full Calendar</div>
  <svg class="body" width="580" height="523" viewBox="349 721 714 643">
    <rect x="365" y="787" width="58" height="22" fill="#f7f7f7" stroke="#ccc"/><path d="M394 787v22" stroke="#ccc"/>
    <path d="M382 793l-4 5 4 5M406 793l4 5-4 5" stroke="#555" fill="none" stroke-width="1.3"/>
    <text x="706" y="803" font-size="17" fill="#333" text-anchor="middle">May 2014</text>
    <rect x="903" y="786" width="144" height="23" fill="#fff" stroke="#ccc"/><rect x="903" y="786" width="58" height="23" fill="var(--red)"/><path d="M1008 786v23" stroke="#ccc"/>
    <g font-size="13" text-anchor="middle"><text x="932" y="802" fill="#fff">month</text><text x="984" y="802" fill="#888">week</text><text x="1027" y="802" fill="#888">day</text></g>
    <rect x="656" y="1007" width="97" height="98" fill="#fcf8e3"/>
    <g stroke="#ddd"><path d="M365 825H1047M365 847H1047M365 927H1047M365 1007H1047M365 1105H1047M365 1185H1047M365 1265H1047M365 1348H1047"/><path d="M365 825V1348M462 825V1348M559 825V1348M656 825V1348M753 825V1348M850 825V1348M947 825V1348M1047 825V1348"/></g>
    <g font-size="13" font-weight="700" fill="#333" text-anchor="middle"><text x="413" y="841">Sun</text><text x="510" y="841">Mon</text><text x="607" y="841">Tue</text><text x="705" y="841">Wed</text><text x="802" y="841">Thu</text><text x="899" y="841">Fri</text><text x="997" y="841">Sat</text></g>
    <g font-size="12" text-anchor="end">
      <g fill="#bbb"><text x="459" y="863">27</text><text x="556" y="863">28</text><text x="653" y="863">29</text><text x="750" y="863">30</text></g>
      <g fill="#333"><text x="847" y="863">1</text><text x="944" y="863">2</text><text x="1044" y="863">3</text>
      <text x="459" y="943">4</text><text x="556" y="943">5</text><text x="653" y="943">6</text><text x="750" y="943">7</text><text x="847" y="943">8</text><text x="944" y="943">9</text><text x="1044" y="943">10</text>
      <text x="459" y="1023">11</text><text x="556" y="1023">12</text><text x="653" y="1023">13</text><text x="750" y="1023">14</text><text x="847" y="1023">15</text><text x="944" y="1023">16</text><text x="1044" y="1023">17</text>
      <text x="459" y="1121">18</text><text x="556" y="1121">19</text><text x="653" y="1121">20</text><text x="750" y="1121">21</text><text x="847" y="1121">22</text><text x="944" y="1121">23</text><text x="1044" y="1121">24</text>
      <text x="459" y="1201">25</text><text x="556" y="1201">26</text><text x="653" y="1201">27</text><text x="750" y="1201">28</text><text x="847" y="1201">29</text><text x="944" y="1201">30</text><text x="1044" y="1201">31</text></g>
      <g fill="#bbb"><text x="459" y="1281">1</text><text x="556" y="1281">2</text><text x="653" y="1281">3</text><text x="750" y="1281">4</text><text x="847" y="1281">5</text><text x="944" y="1281">6</text><text x="1044" y="1281">7</text></g>
    </g>
    <g font-size="11" fill="#fff">
      <rect x="756" y="872" width="289" height="23" fill="#8a8a8a"/><text x="759" y="888"><tspan font-weight="700">10:30a</tspan> Meeting</text>
      <rect x="756" y="897" width="188" height="23" fill="var(--red)"/><text x="759" y="913">All Day Event</text>
      <rect x="853" y="952" width="194" height="23" fill="var(--orange)"/><text x="856" y="968">Long Event</text>
      <rect x="366" y="1032" width="190" height="23" fill="var(--orange)"/><text x="369" y="1048">Long Event</text>
      <rect x="368" y="1057" width="91" height="46" fill="#8a8a8a"/><text x="370" y="1073"><tspan font-weight="700">4p</tspan> Repeating</text><text x="370" y="1095">Event</text>
      <rect x="659" y="1032" width="91" height="23" fill="var(--red)"/><text x="662" y="1048"><tspan font-weight="700">12p</tspan> Lunch</text>
      <rect x="756" y="1032" width="289" height="23" fill="#444"/><text x="759" y="1048"><tspan font-weight="700">2p</tspan> Repeating Event</text>
    </g>
  </svg>
</section>

<footer class="abs footer">Copyright © 2014, Brivel Networks</footer>

</body>
</html>
```